1200 x 150 pixel banner ad max size 200KB

Hi - I'm looking for an animated GIF to be used as an online digital banner advert.

The banner ad is to promote sales of gas cylinders from a world-leading manufacturer.

Headline 1: SLASH YOUR ADMINISTRATION COSTS BY 50%
Headline 2: If you're not happy with our service - we will give you your money back!
Headline 3 (if possible): FREE Regulator for all new customers/vessels

**The banner needs to really stand out of the page and reflect our company and brand - We exist to revolutionise ship safety, performance and crew welfare.**

The banner ad needs to include the product logo and company logo - both attached.

The blue colours in our logos are:
Dark Blue
Pantone 303
C100 M047 Y023 K079
R000 G031 B051
HTML 001F33

Light Blue
Pantone 2995
CO83 M001 Y000 K000
R080 G177 B234
HTML 05B1EA

Target Market(s)

Marine industry buyers - fleet managers, ship owners, technical purchasers, superintendants

Industry/Entity Type

Marine

Requirements
Must have
• Company colours, product and company logo

```html
<!DOCTYPE html>
<html lang="en">
<head>
<meta charset="utf-8">
<title>Corvane Marine – Banner Set</title>
<link rel="stylesheet" href="https://fonts.googleapis.com/css2?family=Arimo:wght@400;700&display=swap">
<style>
  :root {
    --navy: #001f33;
    --navy-soft: #0c3553;
    --navy-panel: #0a2a45;
    --sky: #05b1ea;
    --sky-text: #29b0e8;
    --white: #ffffff;
    --page: #e6e7e9;
    --silver-light: #eef0f2;
    --silver-dark: #9ea4aa;
  }
  * { box-sizing: border-box; margin: 0; padding: 0; }
  html, body {
    width: 1200px;
    height: 1200px;
    overflow: hidden;
    background: var(--page);
    font-family: "Arimo", Arial, sans-serif;
  }
  .banner-stack {
    position: relative;
    width: 1200px;
    height: 1200px;
  }
  .banner {
    position: absolute;
    left: 48px;
    width: 1104px;
    height: 138px;
    display: flex;
    background: var(--white);
    overflow: hidden;
  }
  .banner--costs { top: 222px; }
  .banner--guarantee { top: 524px; }
  .banner--regulator { top: 828px; }

  .banner__edge {
    width: 7px;
    height: 100%;
    background: var(--navy);
    flex: none;
  }
  .brand {
    width: 287px;
    flex: none;
    display: flex;
    flex-direction: column;
    justify-content: center;
    padding-left: 30px;
  }
  .brand__name {
    font-weight: 700;
    font-size: 31px;
    line-height: 1;
    color: var(--sky);
    letter-spacing: -0.5px;
  }
  .brand__tagline {
    margin-top: 8px;
    font-weight: 700;
    font-size: 14.5px;
    color: var(--sky);
  }
  .product-shot {
    position: absolute;
    left: 288px;
    top: 0;
    width: 186px;
    height: 138px;
    background: linear-gradient(90deg, var(--silver-dark) 0%, var(--silver-light) 35%, var(--silver-dark) 55%, var(--silver-light) 80%, var(--silver-dark) 100%);
    z-index: 2;
  }
  .message-panel {
    flex: 1;
    position: relative;
    display: flex;
    align-items: center;
    justify-content: center;
    padding-left: 190px;
    background:
      radial-gradient(ellipse at 35% 40%, rgba(40, 80, 115, 0.55), transparent 60%),
      radial-gradient(ellipse at 85% 60%, rgba(30, 70, 105, 0.45), transparent 55%),
      linear-gradient(90deg, var(--navy-panel), var(--navy-soft) 60%, var(--navy-panel));
  }
  .headline {
    color: var(--sky-text);
    font-size: 24px;
    line-height: 1.35;
    text-align: center;
  }
  .headline--caps { text-transform: uppercase; letter-spacing: -0.2px; }
  .headline--white { color: var(--white); font-size: 24px; }
  .headline strong { font-weight: 700; }
  .headline__accent-white { color: var(--white); font-weight: 700; }
</style>
</head>
<body>
<main class="banner-stack">

  <section class="banner banner--costs">
    <div class="banner__edge"></div>
    <div class="brand">
      <div class="brand__name">Corvane Marine</div>
      <div class="brand__tagline">Innovative Ship Solutions</div>
    </div>
    <div class="product-shot" role="img" aria-label="Group of silver calibration gas cylinders with green caps"></div>
    <div class="message-panel" role="img" aria-label="Faded photo of gas cylinders in dark blue tones">
      <p class="headline headline--caps">Slash your administration costs by <span class="headline__accent-white">50%</span></p>
    </div>
  </section>

  <section class="banner banner--guarantee">
    <div class="banner__edge"></div>
    <div class="brand">
      <div class="brand__name">Corvane Marine</div>
      <div class="brand__tagline">Innovative Ship Solutions</div>
    </div>
    <div class="product-shot" role="img" aria-label="Group of silver calibration gas cylinders with green caps"></div>
    <div class="message-panel" role="img" aria-label="Faded photo of gas cylinders in dark blue tones">
      <p class="headline headline--white">If you're not happy with our service<br>we will give you your money back!</p>
    </div>
  </section>

  <section class="banner banner--regulator">
    <div class="banner__edge"></div>
    <div class="brand">
      <div class="brand__name">Corvane Marine</div>
      <div class="brand__tagline">Innovative Ship Solutions</div>
    </div>
    <div class="product-shot" role="img" aria-label="Group of silver calibration gas cylinders with green caps"></div>
    <div class="message-panel" role="img" aria-label="Faded photo of gas cylinders in dark blue tones">
      <p class="headline"><strong>FREE</strong> Regulator for all new customers/vessels</p>
    </div>
  </section>

</main>
</body>
</html>
```